Harborline Motors LLC

Car Dealer Customer Service
Address: 2741 Linden Avenue, Shelbyville, TN 37162
web: www.harborlinemotorstn.net
email: harborlinemotorstn@mailbox-example.net
Phone: (931) 555-0148
Phone: (629) 555-0173

```html
<!DOCTYPE html>
<html lang="en">
<head>
<meta charset="utf-8">
<title>Harborline Motors LLC – Business Card</title>
<link href="https://fonts.googleapis.com/css2?family=Montserrat:wght@800&family=PT+Sans+Narrow&display=swap" rel="stylesheet">
<style>
  :root {
    --backdrop: #d6d6d6;
    --brand-blue: #1a78b0;
    --brand-blue-light: #2299d8;
    --brand-yellow: #f0bc3b;
    --paper: #ffffff;
  }
  * { box-sizing: border-box; margin: 0; padding: 0; }
  html, body { width: 1200px; height: 846px; overflow: hidden; }
  body {
    background: var(--backdrop);
    position: relative;
    font-family: "PT Sans Narrow", "Arial Narrow", sans-serif;
  }
  .card {
    position: absolute;
    top: 275px;
    width: 520px;
    height: 297px;
    overflow: hidden;
    box-shadow: 0 6px 18px rgba(0,0,0,0.18);
  }
  .card--front { left: 60px; display: flex; }
  .card--back {
    left: 620px;
    background: radial-gradient(circle at 50% 45%, var(--brand-blue-light) 0%, var(--brand-blue) 65%);
    display: flex; flex-direction: column; align-items: center; justify-content: center; gap: 18px;
  }
  .front__brand {
    width: 200px;
    background: var(--paper);
    display: flex; flex-direction: column; align-items: center; justify-content: center; gap: 16px;
  }
  .front__divider { width: 9px; background: var(--brand-yellow); }
  .front__contact {
    flex: 1;
    background: var(--brand-blue);
    color: var(--brand-yellow);
    padding: 48px 20px 0 34px;
    font-size: 16px;
    line-height: 1.45;
  }
  .brand-mark { width: 74px; height: 74px; border-radius: 50%; background: var(--brand-blue); }
  .brand-name {
    font-family: "Montserrat", sans-serif;
    font-weight: 800;
    font-size: 15px;
    letter-spacing: 0.5px;
    color: var(--brand-blue);
    text-align: center;
    line-height: 1.2;
  }
  .contact-list { list-style: none; }
  .contact-list li { display: flex; align-items: center; gap: 9px; white-space: nowrap; }
  .contact-list svg { width: 16px; height: 16px; flex: none; fill: var(--brand-yellow); }
  .contact-address { margin-top: 14px; display: flex; align-items: center; gap: 9px; }
  .contact-address svg { width: 16px; height: 20px; flex: none; fill: var(--brand-yellow); }
  .back__mark { width: 110px; height: 110px; border-radius: 50%; background: var(--brand-blue-light); opacity: .7; }
  .back__name {
    font-family: "Montserrat", sans-serif;
    font-weight: 800;
    font-size: 24px;
    letter-spacing: 1px;
    color: var(--brand-yellow);
  }
</style>
</head>
<body>
  <section class="card card--front" aria-label="Business card front">
    <div class="front__brand">
      <div class="brand-mark" aria-hidden="true"></div>
      <div class="brand-name">HARBORLINE<br>MOTORS</div>
    </div>
    <div class="front__divider"></div>
    <div class="front__contact">
      <ul class="contact-list">
        <li><svg viewBox="0 0 24 24"><path d="M6.6 10.8a15.5 15.5 0 0 0 6.6 6.6l2.2-2.2a1 1 0 0 1 1-.25 11.4 11.4 0 0 0 3.6.57 1 1 0 0 1 1 1V20a1 1 0 0 1-1 1A17 17 0 0 1 3 4a1 1 0 0 1 1-1h3.5a1 1 0 0 1 1 1c0 1.25.2 2.45.57 3.57a1 1 0 0 1-.25 1z"/></svg>(931) 555-0148</li>
        <li><svg viewBox="0 0 24 24"><path d="M6.6 10.8a15.5 15.5 0 0 0 6.6 6.6l2.2-2.2a1 1 0 0 1 1-.25 11.4 11.4 0 0 0 3.6.57 1 1 0 0 1 1 1V20a1 1 0 0 1-1 1A17 17 0 0 1 3 4a1 1 0 0 1 1-1h3.5a1 1 0 0 1 1 1c0 1.25.2 2.45.57 3.57a1 1 0 0 1-.25 1z"/></svg>(629) 555-0173</li>
        <li><svg viewBox="0 0 24 24"><path d="M2 5h20v14H2z M3.5 6.5 12 13l8.5-6.5" fill="none" stroke="#f0bc3b" stroke-width="2"/></svg>harborlinemotorstn@mailbox-example.net</li>
        <li><svg viewBox="0 0 24 24"><g fill="none" stroke="#f0bc3b" stroke-width="2"><circle cx="12" cy="12" r="9.5"/><ellipse cx="12" cy="12" rx="4" ry="9.5"/><path d="M2.5 12h19M4 7h16M4 17h16"/></g></svg>www.harborlinemotorstn.net</li>
      </ul>
      <div class="contact-address">
        <svg viewBox="0 0 16 22"><path d="M8 0a8 8 0 0 0-8 8c0 6 8 14 8 14s8-8 8-14a8 8 0 0 0-8-8zm0 11a3 3 0 1 1 0-6 3 3 0 0 1 0 6z"/></svg>
        <address style="font-style:normal">2741 Linden Avenue,<br>Shelbyville, TN 37162</address>
      </div>
    </div>
  </section>

  <section class="card card--back" aria-label="Business card back">
    <div class="back__mark" aria-hidden="true"></div>
    <div class="back__name">HARBORLINE MOTORS</div>
  </section>
</body>
</html>
```